Medical Simulation - Creative Graphic for Data

My company needs a creative graph that depicts the rationales (or reasons) our learners chose certain drug options. Basically, our clients not only want to know how many times certain drugs were selected, but the "whys" behind their choices. I would like a PPT graphic that I can use for other deliverables, where I can simply switch out the drug (treatment) names, the "whys" (what we call rationales), and the specific metrics (percentages, "n" numbers, etc), and the graphic will update and adjust to the new information. The title of the graph (or the slide where the graph will live) should be something like "Treatment Rationales" or something to that effect. Include a placeholder for text to go if anyone wants to add an analysis of the graphic later. This placeholder should accommodate 2-3 bullet points of text. We want this graphic to not just be an image, but organized in a way that you would see in a presentation slide, with a title, place holder for analysis (as indicated above), branding colors, and helpful information to understand the graphic (what is included in this post and it's associated attachments).

I've included specific drug names, rationales, and metrics to use for this (please see excel document). If you are going to design the graph directly in PPT, please use the PPT template design included. Please don't feel like you have to use 1 slide only or can have multiple graphs, if that makes sense for you design idea. They just need to fit within the coloring of the PPT. For font, please use Arial. Below is a Google Drive Link to branding colors and vector art.

https://files.brivoshare.net/open?id=4KQ2TrLm8-XpVd71sNcYhWuPzAe

We are open to many variations and design ideas. Please don't feel like you have to limit yourself! I've attached a few ideas that we've had and it may be a good place to start. We would ESPECIALLY like to see a version utilizing the radial graph (similar to the one included in the Rationales_DesignIdeas document).

Please reach out if you have any questions. Thanks!

Industry/Entity Type

Drug

Requirements
Nice to have
• It would be great to see the radial graph as a design variation (see link below)
• http://6.plotvenna.com/products/plotvenna/docs/users-guide/img/Samples/radar-chart-fixed-radius.png

```html
<!DOCTYPE html>
<html lang="en">
<head>
<meta charset="utf-8">
<title>Treatment Rationale Data</title>
<link href="https://fonts.googleapis.com/css2?family=Arimo:wght@400;700&display=swap" rel="stylesheet">
<style>
  :root{
    --navy:#0d3b58;
    --blue:#176a9e;
    --slate:#5a5a5c;
    --silver:#a5a5a7;
    --orange:#f6973f;
    --ink:#1f1f1f;
    --title:#555555;
    --backdrop-center:#fafafa;
    --backdrop-edge:#e2e3e4;
    --white:#ffffff;
  }
  html,body{margin:0;padding:0;width:1200px;height:1200px;overflow:hidden;}
  body{background:radial-gradient(ellipse at center,var(--backdrop-center) 45%,var(--backdrop-edge) 100%);}
  .slide-canvas{display:block;width:1200px;height:1200px;font-family:"Arimo",Arial,sans-serif;}
  .slide-title{font-size:46px;font-weight:700;fill:var(--title);}
  .brand-name{font-size:18px;font-weight:400;fill:var(--navy);text-anchor:end;}
  .treatment-heading{font-size:20px;font-weight:700;fill:var(--orange);}
  .treatment-name{font-size:19.3px;fill:var(--ink);}
  .leader{stroke:var(--orange);stroke-width:3;stroke-dasharray:0 7.5;stroke-linecap:round;fill:none;}
  .leader-dot{fill:var(--orange);}
  .count-bar{fill:var(--orange);}
  .count-label{font-size:16px;fill:var(--white);text-anchor:end;}
  .ring{fill:none;stroke-width:22;}
  .seg-navy{stroke:var(--navy);}
  .seg-blue{stroke:var(--blue);}
  .seg-slate{stroke:var(--slate);}
  .seg-silver{stroke:var(--silver);}
  .pct-pill rect{rx:10;ry:10;}
  .pct-pill text{font-size:14px;fill:var(--white);text-anchor:middle;}
  .pill-navy{fill:var(--navy);}
  .pill-blue{fill:var(--blue);}
  .pill-slate{fill:var(--slate);}
  .pill-silver{fill:var(--silver);}
  .legend-heading{font-size:18px;font-weight:700;fill:var(--white);}
  .legend-item{font-size:19px;fill:var(--ink);}
  .note-orange{font-size:15px;fill:var(--orange);}
  .note-navy{font-size:15px;fill:var(--navy);}
  .footer-text{font-size:14.5px;fill:#dfe8ef;text-anchor:middle;}
</style>
</head>
<body>
<svg class="slide-canvas" viewBox="0 0 1500 1500" xmlns="http://www.w3.org/2000/svg" role="img" aria-label="Treatment rationale radial chart slide">
  <defs>
    <linearGradient id="titleRule" x1="0" x2="1">
      <stop offset="0" stop-color="#cfcfcf"/>
      <stop offset="0.7" stop-color="#e6e6e6"/>
      <stop offset="1" stop-color="#ffffff" stop-opacity="0"/>
    </linearGradient>
    <filter id="pillShadow" x="-20%" y="-20%" width="150%" height="160%">
      <feDropShadow dx="1.5" dy="2" stdDeviation="1.5" flood-color="#000" flood-opacity="0.3"/>
    </filter>
  </defs>

  <!-- Slide frame -->
  <rect class="slide" x="50" y="225" width="1400" height="1050" fill="#ffffff"/>
  <rect class="header-bar" x="50" y="225" width="1400" height="33" fill="var(--navy)"/>
  <text class="brand-name" x="1420" y="282">Clinvara</text>
  <rect x="50" y="286" width="1000" height="3" fill="url(#titleRule)"/>
  <rect x="50" y="434" width="1000" height="3" fill="url(#titleRule)"/>
  <text class="slide-title" x="213" y="375">Rationale Data</text>

  <!-- Radial rationale rings -->
  <g class="rings">
    <g>
      <path class="ring seg-navy"   pathLength="100" stroke-dasharray="17.6 200" stroke-dashoffset="0"     d="M1000 821 A66 66 0 1 0 944.6 719.1"/>
      <path class="ring seg-blue"   pathLength="100" stroke-dasharray="35.4 200" stroke-dashoffset="-18"   d="M1000 821 A66 66 0 1 0 944.6 719.1"/>
      <path class="ring seg-slate"  pathLength="100" stroke-dasharray="17.6 200" stroke-dashoffset="-54.5" d="M1000 821 A66 66 0 1 0 944.6 719.1"/>
      <path class="ring seg-silver" pathLength="100" stroke-dasharray="27.6 200" stroke-dashoffset="-72.5" d="M1000 821 A66 66 0 1 0 944.6 719.1"/>
    </g>
    <g>
      <path class="ring seg-navy"   pathLength="100" stroke-dasharray="49.6 200" stroke-dashoffset="0"   d="M1000 856 A101 101 0 1 0 915.3 700"/>
      <path class="ring seg-blue"   pathLength="100" stroke-dasharray="16.2 200" stroke-dashoffset="-50" d="M1000 856 A101 101 0 1 0 915.3 700"/>
      <path class="ring seg-slate"  pathLength="100" stroke-dasharray="16.2 200" stroke-dashoffset="-66.6" d="M1000 856 A101 101 0 1 0 915.3 700"/>
      <path class="ring seg-silver" pathLength="100" stroke-dasharray="16.8 200" stroke-dashoffset="-83.2" d="M1000 856 A101 101 0 1 0 915.3 700"/>
    </g>
    <g>
      <path class="ring seg-navy"   pathLength="100" stroke-dasharray="18.6 200" stroke-dashoffset="0"   d="M1000 891 A136 136 0 1 0 885.9 680.9"/>
      <path class="ring seg-blue"   pathLength="100" stroke-dasharray="16.6 200" stroke-dashoffset="-19" d="M1000 891 A136 136 0 1 0 885.9 680.9"/>
      <path class="ring seg-slate"  pathLength="100" stroke-dasharray="25.6 200" stroke-dashoffset="-36" d="M1000 891 A136 136 0 1 0 885.9 680.9"/>
      <path class="ring seg-silver" pathLength="100" stroke-dasharray="38 200"   stroke-dashoffset="-62" d="M1000 891 A136 136 0 1 0 885.9 680.9"/>
    </g>
    <g>
      <path class="ring seg-navy"   pathLength="100" stroke-dasharray="7.7 200"  stroke-dashoffset="0"   d="M1000 925 A170 170 0 1 0 857.4 662.4"/>
      <path class="ring seg-blue"   pathLength="100" stroke-dasharray="7.7 200"  stroke-dashoffset="-8"  d="M1000 925 A170 170 0 1 0 857.4 662.4"/>
      <path class="ring seg-slate"  pathLength="100" stroke-dasharray="41.7 200" stroke-dashoffset="-16" d="M1000 925 A170 170 0 1 0 857.4 662.4"/>
      <path class="ring seg-silver" pathLength="100" stroke-dasharray="42 200"   stroke-dashoffset="-58" d="M1000 925 A170 170 0 1 0 857.4 662.4"/>
    </g>
    <g>
      <path class="ring seg-slate"  pathLength="100" stroke-dasharray="49.8 200" stroke-dashoffset="0"   d="M1000 960 A205 205 0 1 0 828.1 643.4"/>
      <path class="ring seg-silver" pathLength="100" stroke-dasharray="50 200"   stroke-dashoffset="-50" d="M1000 960 A205 205 0 1 0 828.1 643.4"/>
    </g>
    <g>
      <path class="ring seg-navy"   pathLength="100" stroke-dasharray="49.8 200" stroke-dashoffset="0"   d="M1000 994 A239 239 0 1 0 799.6 624.8"/>
      <path class="ring seg-blue"   pathLength="100" stroke-dasharray="50 200"   stroke-dashoffset="-50" d="M1000 994 A239 239 0 1 0 799.6 624.8"/>
    </g>
    <g>
      <path class="ring seg-blue"   pathLength="100" stroke-dasharray="49.8 200" stroke-dashoffset="0"   d="M1000 1028 A273 273 0 1 0 771 606.3"/>
      <path class="ring seg-silver" pathLength="100" stroke-dasharray="50 200"   stroke-dashoffset="-50" d="M1000 1028 A273 273 0 1 0 771 606.3"/>
    </g>
  </g>

  <!-- Percentage pills -->
  <g class="pct-labels" filter="url(#pillShadow)">
    <g class="pct-pill"><rect class="pill-navy"   x="1011" y="815" width="42" height="20"/><text x="1032" y="830">18%</text></g>
    <g class="pct-pill"><rect class="pill-blue"   x="1058" y="711" width="42" height="20"/><text x="1079" y="726">36%</text></g>
    <g class="pct-pill"><rect class="pill-slate"  x="1014" y="679" width="42" height="20"/><text x="1035" y="694">18%</text></g>
    <g class="pct-pill"><rect class="pill-silver" x="949"  y="703" width="42" height="20"/><text x="970"  y="718">27%</text></g>

    <g class="pct-pill"><rect class="pill-navy"   x="1095" y="733" width="42" height="20"/><text x="1116" y="748">50%</text></g>
    <g class="pct-pill"><rect class="pill-blue"   x="1044" y="649" width="42" height="20"/><text x="1065" y="664">17%</text></g>
    <g class="pct-pill"><rect class="pill-slate"  x="974"  y="648" width="42" height="20"/><text x="995"  y="663">17%</text></g>
    <g class="pct-pill"><rect class="pill-silver" x="918"  y="676" width="42" height="20"/><text x="939"  y="691">17%</text></g>

    <g class="pct-pill"><rect class="pill-navy"   x="1072" y="861" width="42" height="20"/><text x="1093" y="876">19%</text></g>
    <g class="pct-pill"><rect class="pill-blue"   x="1131" y="769" width="42" height="20"/><text x="1152" y="784">17%</text></g>
    <g class="pct-pill"><rect class="pill-slate"  x="1096" y="647" width="42" height="20"/><text x="1117" y="662">26%</text></g>
    <g class="pct-pill"><rect class="pill-silver" x="901"  y="649" width="42" height="20"/><text x="922"  y="664">38%</text></g>

    <g class="pct-pill"><rect class="pill-navy"   x="1015" y="920" width="38" height="20"/><text x="1034" y="935">8%</text></g>
    <g class="pct-pill"><rect class="pill-blue"   x="1077" y="899" width="38" height="20"/><text x="1096" y="914">8%</text></g>
    <g class="pct-pill"><rect class="pill-slate"  x="1125" y="622" width="42" height="20"/><text x="1146" y="637">42%</text></g>
    <g class="pct-pill"><rect class="pill-silver" x="880"  y="621" width="42" height="20"/><text x="901"  y="636">42%</text></g>

    <g class="pct-pill"><rect class="pill-slate"  x="1189" y="669" width="42" height="20"/><text x="1210" y="684">50%</text></g>
    <g class="pct-pill"><rect class="pill-silver" x="826"  y="631" width="42" height="20"/><text x="847"  y="646">50%</text></g>

    <g class="pct-pill"><rect class="pill-navy"   x="1217" y="641" width="42" height="20"/><text x="1238" y="656">50%</text></g>
    <g class="pct-pill"><rect class="pill-blue"   x="806"  y="604" width="42" height="20"/><text x="827"  y="619">50%</text></g>

    <g class="pct-pill"><rect class="pill-blue"   x="1246" y="616" width="42" height="20"/><text x="1267" y="631">50%</text></g>
    <g class="pct-pill"><rect class="pill-silver" x="779"  y="578" width="42" height="20"/><text x="800"  y="593">50%</text></g>
  </g>

  <!-- Treatment list -->
  <text class="treatment-heading" x="208" y="792">Treatment*</text>
  <g class="treatments">
    <text class="treatment-name" x="208" y="827">irinotecan/leucovorin/5-FU plus bevacizumab</text>
    <line class="leader" x1="603" y1="821" x2="664" y2="821"/><circle class="leader-dot" cx="672" cy="821" r="5"/>
    <rect class="count-bar" x="691" y="810" width="306" height="23"/><text class="count-label" x="988" y="828">n = 100</text>

    <text class="treatment-name" x="208" y="862">oxaliplatin/capecitabine</text>
    <line class="leader" x1="420" y1="856" x2="753" y2="856"/><circle class="leader-dot" cx="761" cy="856" r="5"/>
    <rect class="count-bar" x="778" y="845" width="219" height="23"/><text class="count-label" x="980" y="863">n = 70</text>

    <text class="treatment-name" x="208" y="897">oxaliplatin/leucovorin/5-FU plus bevacizumab</text>
    <line class="leader" x1="606" y1="891" x2="811" y2="891"/><circle class="leader-dot" cx="819" cy="891" r="5"/>
    <rect class="count-bar" x="837" y="880" width="160" height="23"/><text class="count-label" x="980" y="898">n = 50</text>

    <text class="treatment-name" x="208" y="932">oxaliplatin/capecitabine plus bevacizumab</text>
    <line class="leader" x1="578" y1="925" x2="815" y2="925"/><circle class="leader-dot" cx="823" cy="925" r="5"/>
    <rect class="count-bar" x="837" y="914" width="160" height="23"/><text class="count-label" x="980" y="932">n = 50</text>

    <text class="treatment-name" x="208" y="967">oxaliplatin/leucovorin/5-FU</text>
    <line class="leader" x1="443" y1="960" x2="870" y2="960"/><circle class="leader-dot" cx="878" cy="960" r="5"/>
    <rect class="count-bar" x="896" y="949" width="101" height="23"/><text class="count-label" x="980" y="967">n = 30</text>

    <text class="treatment-name" x="208" y="1001">irinotecan/leucovorin/5-FU plus cetuximab</text>
    <line class="leader" x1="581" y1="994" x2="868" y2="994"/><circle class="leader-dot" cx="876" cy="994" r="5"/>
    <rect class="count-bar" x="896" y="983" width="101" height="23"/><text class="count-label" x="980" y="1001">n = 30</text>

    <text class="treatment-name" x="208" y="1036">irinotecan</text>
    <line class="leader" x1="299" y1="1028" x2="900" y2="1028"/><circle class="leader-dot" cx="908" cy="1028" r="5"/>
    <rect class="count-bar" x="925" y="1017" width="72" height="23"/><text class="count-label" x="980" y="1035">n = 20</text>
  </g>

  <!-- Legend -->
  <g class="legend">
    <rect x="1050" y="1063" width="348" height="34" rx="17" fill="var(--navy)"/>
    <text class="legend-heading" x="1080" y="1086">Rationales*</text>
    <rect x="1058" y="1110" width="16" height="16" fill="var(--navy)"/>
    <text class="legend-item" x="1087" y="1126">Fewer overall side effects</text>
    <rect x="1058" y="1137" width="16" height="16" fill="var(--blue)"/>
    <text class="legend-item" x="1087" y="1153">Impact on quality of life</text>
    <rect x="1058" y="1165" width="16" height="16" fill="var(--slate)"/>
    <text class="legend-item" x="1087" y="1180">Preserves future treatment options</text>
    <rect x="1058" y="1192" width="16" height="16" fill="var(--silver)"/>
    <text class="legend-item" x="1087" y="1208">Recent guidelines</text>
  </g>

  <!-- Notes -->
  <text class="note-orange" x="120" y="1193">*Number of Drug Selections</text>
  <text class="note-navy" x="120" y="1220">*Learners can select 1-2 rationales for each treatment ordered</text>

  <!-- Footer -->
  <rect class="footer-bar" x="50" y="1245" width="1400" height="30" fill="var(--navy)"/>
  <text class="footer-text" x="750" y="1265">Clinvara Education Confidential and Proprietary Information</text>
</svg>
</body>
</html>
```